Derek Mavlow Business card

Hey there, I’m hoping to have a business card designed. I’m in Real estate and just switched to a new Brokerage called: The Property Quarter

The back could just be the company name maybe or whatever looks good!

I’ve attached some logos of our company and some cards my buddy had done up.

On the card:
Derek Mavlow
derekmavlow@postnest.example
587-204-6618
derekmavlow-homes.example

Target Market(s)

Home buyers and sellers

Industry/Entity Type

Real Estate

Contact Information for Business Card

just looking for a cool and modern design with my picture on it. I like the idea of Black and red being used.

Requirements
Must have
• all the details provided. I'm open to anything. Just want a professional looking card.

```html
<!DOCTYPE html>
<html lang="en">
<head>
<meta charset="utf-8">
<title>Derek Mavlow – Business Card</title>
<link rel="stylesheet" href="https://fonts.googleapis.com/css2?family=Cinzel:wght@400;500&family=Montserrat:wght@500;800&display=swap">
<style>
  :root {
    --backdrop: #d1d1d1;
    --card-front: #231f20;
    --card-back: #050607;
    --brand-red: #971a1e;
    --white: #ffffff;
    --mono-grey: #4a4647;
    --icon-grey: #9a9a9a;
  }
  * { margin: 0; padding: 0; box-sizing: border-box; }
  html, body {
    width: 1200px; height: 1200px; overflow: hidden;
    background: var(--backdrop);
  }
  .card {
    position: absolute; left: 114px; width: 971px; height: 554px; overflow: hidden;
  }
  .card--front { top: 30px; background: var(--card-front); }
  .card--back { top: 616px; background: var(--card-back); }

  /* Front */
  .agent-name {
    position: absolute; left: 98px; top: 82px;
    font-family: "Cinzel", serif; font-weight: 400; font-size: 46px;
    letter-spacing: 1px; color: var(--white); white-space: nowrap;
  }
  .agent-name .surname { color: var(--brand-red); margin-left: 16px; }

  .agent-photo {
    position: absolute; left: 470px; top: 180px; width: 190px; height: 300px;
    background: radial-gradient(ellipse 70% 60% at 55% 40%, #8a8687 0%, #5c5859 45%, #353132 80%, rgba(35,31,32,0) 100%);
    -webkit-mask-image: linear-gradient(90deg, transparent 0%, #000 22%, #000 100%);
            mask-image: linear-gradient(90deg, transparent 0%, #000 22%, #000 100%);
  }
  .monogram-name {
    position: absolute; left: 660px; top: 196px; width: 311px;
    font-family: "Cinzel", serif; font-weight: 500; font-size: 60px; line-height: 1.35;
    color: var(--mono-grey); white-space: nowrap;
  }

  .contact-band {
    position: absolute; left: 0; top: 480px; width: 100%; height: 74px;
    background: var(--brand-red);
    display: flex; align-items: center; justify-content: center; gap: 26px;
    font-family: "Montserrat", sans-serif; font-weight: 500; font-size: 20px; color: var(--white);
  }
  .contact-item { display: flex; align-items: center; gap: 9px; white-space: nowrap; }
  .contact-item svg { width: 20px; height: 20px; flex: none; }

  /* Back */
  .brokerage-name {
    position: absolute; left: 80px; top: 78px;
    display: flex; align-items: center; gap: 20px;
    font-family: "Montserrat", sans-serif; font-weight: 800; font-size: 64px; line-height: 1.08;
    letter-spacing: -0.5px; color: var(--white); text-transform: uppercase; white-space: nowrap;
  }
  .brokerage-name .mark { width: 34px; height: 34px; background: var(--brand-red); flex: none; }

  .brand-graphic {
    position: absolute; left: 577px; top: 285px; width: 356px; height: 269px;
    background: radial-gradient(ellipse 60% 70% at 55% 45%, #3e3c3d 0%, #262425 50%, rgba(5,6,7,0) 100%);
    -webkit-mask-image: linear-gradient(180deg, #000 55%, transparent 100%);
            mask-image: linear-gradient(180deg, #000 55%, transparent 100%);
  }
</style>
</head>
<body>
  <section class="card card--front">
    <h1 class="agent-name">Derek<span class="surname">Mavlow</span></h1>
    <div class="monogram-name">Derek<br>Mavlow</div>
    <div class="agent-photo" role="img" aria-label="Black and white portrait photo of the agent in a dark suit"></div>
    <div class="contact-band">
      <span class="contact-item">
        <svg viewBox="0 0 20 20" fill="none" stroke="var(--icon-grey)" stroke-width="1.4"><circle cx="10" cy="10" r="8.5"/><path d="M7 6.2l1.4-.4 1 2.2-.9.8c.5 1.1 1.3 1.9 2.4 2.4l.8-.9 2.2 1-.4 1.4c-3 .4-6.5-3.1-5.5-6.5z"/></svg>
        587-204-6618
      </span>
      <span class="contact-item">
        <svg viewBox="0 0 20 20" fill="none" stroke="var(--icon-grey)" stroke-width="1.4"><rect x="2" y="4.5" width="16" height="11"/><path d="M2 4.5l8 6.5 8-6.5M2 15.5l6-5M18 15.5l-6-5"/></svg>
        derekmavlow@postnest.example
      </span>
      <span class="contact-item">
        <svg viewBox="0 0 20 20" fill="none" stroke="var(--icon-grey)" stroke-width="1.4"><circle cx="10" cy="10" r="8.5"/><ellipse cx="10" cy="10" rx="3.8" ry="8.5"/><path d="M1.5 10h17M3 5.5h14M3 14.5h14"/></svg>
        derekmavlow-homes.example
      </span>
    </div>
  </section>

  <section class="card card--back">
    <div class="brokerage-name">
      <span class="mark"></span>
      <span>The Property<br>Quarter</span>
    </div>
    <div class="brand-graphic" role="img" aria-label="Brokerage emblem area in dark grey tones"></div>
  </section>
</body>
</html>
```